Making 6 Posters and 2 large posters for coffee shop

We are Brindle Mug Depot (similar to a brewhollow), planning to make 3 boards for menu, 3 photos to be printed onto the board, and 2 large posters. (dimensions provided). We believe this is a very simple project with not much additional work required as all pictures have been provided.
We are asking for minimalist design. Very simple. All photos have been provided. 3 of the boards, and 2 for the large posters. The menu has been done but it is in PDF and require recreation (pls make similar design)
The menu board and the 3 other photos are roughly square shape. While dimensions are not provided by our contractors yet, designers can roughly get the dimension from the photos of the boards we are planning to replace.
All these posters will be printed with no frames. So it will look something like those menu board at brewhollow.
Urgently need it in next 24 hours.
Instructions all in PPT attached.
File Link provided:
http://qlinkbox.example/7hT3kWz
Thanks.
---- Edited
For the pictures, we are looking for borders like this if possible (VORN - expensive looking border but platinum white, and dark background.) for the large poster, we liek black themed background with some glow if possible around the cups like the kelvaro logo)
http://www.plumtemplates.example/images/thumbs/Onyx-Slate-psd48213.png
http://www.wirefable-news.example/wp-content/uploads/2013/11/kelvaro-signage.jpg
Target Market(s)
Professionals - Lawyers, Bankers, Brokers
Industry/Entity Type
Coffee Shop

```html
<!DOCTYPE html>
<html lang="en">
<head>
<meta charset="utf-8">
<title>Brindle Mug Depot Menu Board</title>
<link href="https://fonts.googleapis.com/css2?family=Questrial&family=Open+Sans:wght@700&display=swap" rel="stylesheet">
<style>
  :root {
    --paper: #fdf8b2;
    --frame-orange: #f08a4b;
    --frame-plum: #8e1f6e;
    --header-magenta: #b3127c;
    --header-coral: #e8505b;
    --header-orange: #f9a23e;
    --ink: #15121c;
    --banner-dark: #1f1a29;
    --fold-grey: #d8d4c6;
    --bar-pink: #d93a6c;
    --bar-orange: #f9a548;
    --drinks-yellow: #fee42e;
    --ribbon-brown: #8b5a2b;
    --ribbon-dark: #5b3311;
    --white: #ffffff;
  }
  html, body {
    margin: 0;
    padding: 0;
    width: 1200px;
    height: 1200px;
    overflow: hidden;
    background: var(--paper);
  }
  .menu-board {
    position: relative;
    width: 1200px;
    height: 1200px;
    background: var(--paper);
    font-family: "Questrial", "Century Gothic", sans-serif;
    color: var(--ink);
  }
  .board-shapes {
    position: absolute;
    inset: 0;
  }
  .board-title,
  .section-title,
  .ribbon-title {
    position: absolute;
    margin: 0;
    font-family: "Open Sans", Arial, sans-serif;
    font-weight: 700;
    color: var(--white);
    text-align: center;
  }
  .board-title {
    left: 420px; width: 354px; top: 64px; height: 74px;
    line-height: 74px; font-size: 64px; letter-spacing: 1px;
  }
  .section-title {
    left: 468px; width: 264px; height: 48px;
    line-height: 48px; font-size: 30px; letter-spacing: 0.5px;
  }
  .ribbon-title {
    height: 69px; line-height: 69px; font-size: 31px;
  }
  .item-list {
    position: absolute;
    margin: 0;
    padding: 0;
    list-style: none;
    font-size: 39px;
  }
  .item {
    display: flex;
    align-items: baseline;
    height: 62px;
    white-space: nowrap;
  }
  .item-name { flex: none; }
  .item-leader {
    flex: 1 1 auto;
    overflow: hidden;
    margin: 0 6px 0 4px;
  }
  .item-leader::after {
    content: "....................................................................................................";
    letter-spacing: 1px;
  }
  .item-price { flex: none; }
  .salad-list { left: 198px; width: 798px; top: 284px; }
  .sandwich-list { left: 198px; width: 798px; top: 584px; }
  .hot-list { left: 66px; width: 484px; top: 954px; }
  .juice-list { left: 646px; width: 484px; top: 954px; }
</style>
</head>
<body>
<main class="menu-board">
  <svg class="board-shapes" width="1200" height="1200" viewBox="0 0 1200 1200" aria-hidden="true">
    <defs>
      <linearGradient id="header-gradient" x1="0" y1="0" x2="1" y2="0">
        <stop offset="0" stop-color="var(--header-magenta)"/>
        <stop offset="0.5" stop-color="var(--header-coral)"/>
        <stop offset="1" stop-color="var(--header-orange)"/>
      </linearGradient>
      <linearGradient id="bar-left" x1="0" y1="0" x2="1" y2="0">
        <stop offset="0" stop-color="var(--bar-pink)"/>
        <stop offset="1" stop-color="#e55a72"/>
      </linearGradient>
      <linearGradient id="bar-right" x1="0" y1="0" x2="1" y2="0">
        <stop offset="0" stop-color="#f68a3a"/>
        <stop offset="1" stop-color="#fbc46c"/>
      </linearGradient>
    </defs>

    <!-- frames -->
    <rect class="frame-outer" x="32" y="32" width="1136" height="1136" fill="none" stroke="var(--frame-orange)" stroke-width="2"/>
    <rect class="frame-inner" x="42" y="42" width="1116" height="1116" fill="none" stroke="var(--frame-plum)" stroke-width="2"/>

    <!-- header band -->
    <rect class="header-band" x="43" y="43" width="1114" height="145" fill="url(#header-gradient)"/>

    <!-- title banner -->
    <polygon points="366,88 440,88 440,156 366,156 394,122" fill="var(--banner-dark)"/>
    <polygon points="834,88 760,88 760,156 834,156 806,122" fill="var(--banner-dark)"/>
    <polygon points="420,138 462,138 462,156" fill="var(--fold-grey)"/>
    <polygon points="774,138 732,138 732,156" fill="var(--fold-grey)"/>
    <rect x="420" y="66" width="354" height="72" fill="var(--banner-dark)"/>

    <!-- salads section header -->
    <g class="section-header" transform="translate(0,218)">
      <rect x="334" y="12" width="110" height="24" fill="url(#bar-left)"/>
      <rect x="756" y="12" width="110" height="24" fill="url(#bar-right)"/>
      <polyline points="430,4 450,24 430,44" fill="none" stroke="var(--banner-dark)" stroke-width="5"/>
      <polyline points="442,4 462,24 442,44" fill="none" stroke="var(--banner-dark)" stroke-width="5"/>
      <polyline points="770,4 750,24 770,44" fill="none" stroke="var(--banner-dark)" stroke-width="5"/>
      <polyline points="758,4 738,24 758,44" fill="none" stroke="var(--banner-dark)" stroke-width="5"/>
      <polygon points="456,0 744,0 732,24 744,48 456,48 468,24" fill="var(--banner-dark)"/>
    </g>

    <!-- sandwich section header -->
    <g class="section-header" transform="translate(0,518)">
      <rect x="334" y="12" width="110" height="24" fill="url(#bar-left)"/>
      <rect x="756" y="12" width="110" height="24" fill="url(#bar-right)"/>
      <polyline points="430,4 450,24 430,44" fill="none" stroke="var(--banner-dark)" stroke-width="5"/>
      <polyline points="442,4 462,24 442,44" fill="none" stroke="var(--banner-dark)" stroke-width="5"/>
      <polyline points="770,4 750,24 770,44" fill="none" stroke="var(--banner-dark)" stroke-width="5"/>
      <polyline points="758,4 738,24 758,44" fill="none" stroke="var(--banner-dark)" stroke-width="5"/>
      <polygon points="456,0 744,0 732,24 744,48 456,48 468,24" fill="var(--banner-dark)"/>
    </g>

    <!-- drinks panel -->
    <rect class="drinks-panel" x="43" y="806" width="1114" height="351" fill="var(--drinks-yellow)"/>
    <rect class="drinks-divider" x="43" y="802" width="1114" height="6" fill="var(--frame-plum)"/>

    <!-- hot drinks ribbon -->
    <polygon points="66,876 130,876 130,934 66,934 86,905" fill="var(--ribbon-dark)"/>
    <polygon points="438,876 374,876 374,934 438,934 418,905" fill="var(--ribbon-dark)"/>
    <polygon points="108,922 144,922 144,934" fill="var(--white)"/>
    <polygon points="396,922 360,922 360,934" fill="var(--white)"/>
    <rect x="108" y="853" width="288" height="69" fill="var(--ribbon-brown)"/>

    <!-- coffee cup icon -->
    <g class="icon-cup" fill="var(--ribbon-brown)">
      <path d="M482 886 h56 v26 a18 18 0 0 1 -18 18 h-20 a18 18 0 0 1 -18 -18 z"/>
      <path d="M538 892 a12 12 0 0 1 0 24" fill="none" stroke="var(--ribbon-brown)" stroke-width="6"/>
      <rect x="470" y="928" width="82" height="5" rx="2"/>
      <path d="M504 878 c-8 -8 8 -14 0 -24 c-6 -8 6 -12 2 -20" fill="none" stroke="var(--ribbon-brown)" stroke-width="3"/>
      <path d="M516 878 c-6 -6 6 -10 0 -18" fill="none" stroke="var(--ribbon-brown)" stroke-width="3"/>
    </g>

    <!-- juices ribbon -->
    <polygon points="648,876 712,876 712,934 648,934 668,905" fill="var(--ribbon-dark)"/>
    <polygon points="1026,876 962,876 962,934 1026,934 1006,905" fill="var(--ribbon-dark)"/>
    <polygon points="690,922 726,922 726,934" fill="var(--white)"/>
    <polygon points="978,922 942,922 942,934" fill="var(--white)"/>
    <rect x="690" y="853" width="288" height="69" fill="var(--ribbon-brown)"/>

    <!-- juice glass icon -->
    <g class="icon-juice" fill="var(--ribbon-brown)">
      <circle cx="1122" cy="856" r="14"/>
      <line x1="1090" y1="860" x2="1068" y2="826" stroke="var(--ribbon-brown)" stroke-width="5"/>
      <rect x="1058" y="856" width="66" height="6"/>
      <polygon points="1064,866 1118,866 1110,936 1072,936"/>
    </g>
  </svg>

  <h1 class="board-title">MENU</h1>

  <h2 class="section-title" style="top:218px">SALADS</h2>
  <ul class="item-list salad-list">
    <li class="item"><span class="item-name">Brindle Mug Salad</span><span class="item-leader"></span><span class="item-price">0.00 $</span></li>
    <li class="item"><span class="item-name">Brindle Mug Salad</span><span class="item-leader"></span><span class="item-price">0.00 $</span></li>
    <li class="item"><span class="item-name">Brindle Mug Salad</span><span class="item-leader"></span><span class="item-price">0.00 $</span></li>
  </ul>

  <h2 class="section-title" style="top:518px">SANDWICH</h2>
  <ul class="item-list sandwich-list">
    <li class="item"><span class="item-name">Vegetarian Sandwich</span><span class="item-leader"></span><span class="item-price">0.00 $</span></li>
    <li class="item"><span class="item-name">Vegetarian Sandwich</span><span class="item-leader"></span><span class="item-price">0.00 $</span></li>
    <li class="item"><span class="item-name">Vegetarian Sandwich</span><span class="item-leader"></span><span class="item-price">0.00 $</span></li>
  </ul>

  <h2 class="ribbon-title" style="left:108px; width:288px; top:853px">HOT DRINKS</h2>
  <ul class="item-list hot-list">
    <li class="item"><span class="item-name">Cappauccino</span><span class="item-leader"></span><span class="item-price">0.00 $</span></li>
    <li class="item"><span class="item-name">Cappauccino</span><span class="item-leader"></span><span class="item-price">0.00 $</span></li>
    <li class="item"><span class="item-name">Cappauccino</span><span class="item-leader"></span><span class="item-price">0.00 $</span></li>
  </ul>

  <h2 class="ribbon-title" style="left:690px; width:288px; top:853px">JUICES</h2>
  <ul class="item-list juice-list">
    <li class="item"><span class="item-name">Fresh Orange</span><span class="item-leader"></span><span class="item-price">0.00 $</span></li>
    <li class="item"><span class="item-name">Fresh Orange</span><span class="item-leader"></span><span class="item-price">0.00 $</span></li>
    <li class="item"><span class="item-name">Fresh Orange</span><span class="item-leader"></span><span class="item-price">0.00 $</span></li>
  </ul>
</main>
</body>
</html>
```